KLV Messaging - veteran and exclusive boutique copywriting agency

PROJECT NEEDS:
1. Website design - full homepage design and inner page top banner design
2. Logo design
* Please see attached Briefs (Word Docs) for descriptions of what is needed for 1 and 2 above.
ABOUT THE CLIENT:
KLV Messaging is a veteran and exclusive boutique copywriting agency run by Marcus Holloway. Marcus is an award-winning published novelist and an accomplished executive ghostwriter with articles regularly published prominent technology publications like Brisk, ByteHarbor, FoundryPulse, and more. For nearly three decades, Marcus has focused solely on the technology sector - serving clients in Israel, Europe and the US.

Target Market(s)

hi-tech companies run by serious, confident professionals.

Industry/Entity Type

Business

Number of Pages Required

2 page

Font styles to use
Sans Serif
Other font styles liked:
• font should be modern

Colors
0054AA
0677BA
7BADD7
CADEEF
E8F1F8
F0912C
F2A743
F7CA91
FBE8D2
FDF5EE

Requirements
Must have
• psd files for logo, homepage design, and inner page top banner design
Nice to have
• Please see attached Website and Logo Design Briefs (Word Docs)
Should not have

```html
<!DOCTYPE html>
<html lang="en">
<head>
<meta charset="utf-8">
<title>KLV Messaging</title>
<link href="https://fonts.googleapis.com/css2?family=Poppins:wght@400;500;600;700&display=swap" rel="stylesheet">
<style>
:root{
  --blue:#0677BA;
  --blue-deep:#0054AA;
  --blue-soft:#7BADD7;
  --blue-pale:#CADEEF;
  --orange:#F0912C;
  --orange-light:#F2A743;
  --navy:#13161f;
  --grey-bg:#ececed;
  --text:#6f6f6f;
  --ink:#222;
  --white:#fff;
}
*{margin:0;padding:0;box-sizing:border-box}
html,body{width:1200px;height:3698px;overflow:hidden}
body{position:relative;font-family:'Poppins',sans-serif;background:var(--white);color:var(--ink)}
.abs{position:absolute}
.top-bar{left:0;top:0;width:1200px;height:11px;background:var(--blue)}
.brand{left:86px;top:24px;line-height:1}
.brand-name{font-size:40px;font-weight:700;color:var(--blue);letter-spacing:1px}
.brand-sub{font-size:9px;font-weight:600;color:var(--orange);letter-spacing:.5px;display:block;margin-top:2px}
.main-nav{left:503px;top:38px;display:flex;gap:29px;font-size:14px;color:#444}
.social{display:flex;gap:5px}
.social span{width:28px;height:28px;border-radius:50%;background:var(--blue);display:block}
.social.head{left:988px;top:33px}
.hero-bg{left:0;top:89px}
.hero-photo{left:861px;top:115px;width:273px;height:423px;border-radius:40% 40% 8px 8px;background:radial-gradient(circle at 50% 35%,#6f8fb2 0%,#3a5878 45%,#1a1f2b 80%)}
.hero-title{left:87px;top:232px;font-size:43px;font-weight:700;color:var(--white);letter-spacing:-.5px}
.hero-title em{font-style:normal;color:var(--blue)}
.hero-sub{left:87px;top:298px;font-size:16px;line-height:26px;color:var(--white)}
.btn{background:var(--blue);color:var(--white);font-weight:500;display:flex;align-items:center;justify-content:center}
.hero-btn{left:88px;top:376px;width:162px;height:51px;font-size:15px}
.section-title{left:0;width:1200px;text-align:center;font-size:31px;font-weight:700;color:var(--blue)}
.section-title em{font-style:normal;color:var(--orange)}
.client{font-size:26px;font-weight:600;color:#1d2a5a;width:190px;text-align:center;display:flex;align-items:center;justify-content:center;gap:8px}
.client i{width:14px;height:14px;border-radius:50%;background:var(--orange);display:block}
.arrow{width:30px;height:40px}
.grey-band{left:0;width:1200px;background:var(--grey-bg)}
.card{top:1227px;width:326px;height:400px;background:var(--white)}
.card-photo{width:230px;height:230px;border-radius:50%;background:radial-gradient(circle at 50% 40%,#c9c4b8,#6f7a6a 75%)}
.card-icon{width:78px;height:78px;border-radius:50%;background:var(--orange);display:flex;align-items:center;justify-content:center}
.card-title{width:326px;text-align:center;font-size:15px;font-weight:600;color:var(--blue)}
.card-text{width:326px;text-align:center;font-size:14px;line-height:20px;color:var(--text)}
.card-btn{width:124px;height:38px;font-size:13px;font-weight:600}
.why-bg{left:0;top:1729px;width:1200px;height:685px;background:linear-gradient(135deg,#3d8fc8 0%,#1c78b8 60%,#2a82c0 100%)}
.why-title{left:132px;top:1860px;font-size:31px;font-weight:700;color:var(--orange)}
.why-text{left:132px;top:1918px;width:540px;font-size:16px;line-height:26px;color:var(--white)}
.why-list{left:132px;top:2044px;list-style:none;font-size:16px;line-height:31px;color:var(--white)}
.why-list li{display:flex;align-items:center;gap:13px}
.why-list li::before{content:"";width:10px;height:10px;border-radius:50%;background:var(--orange);box-shadow:0 0 0 2px rgba(242,167,67,.45)}
.why-photo{left:756px;top:1774px;width:359px;height:612px;border-radius:50%;background:radial-gradient(ellipse at 50% 40%,#6f97c4 0%,#3b5c86 50%,#1e2c45 100%)}
.quote-circle{left:136px;top:2622px;width:158px;height:158px;border-radius:50%;background:var(--blue-soft)}
.quote-mark{left:156px;top:2655px;font-size:90px;font-weight:700;color:var(--white);line-height:1}
.client-photo{left:228px;top:2625px;width:152px;height:152px;border-radius:50%;background:radial-gradient(circle at 50% 40%,#e8e2d8,#a9b79c 80%);border:3px solid var(--grey-bg)}
.quote-text{left:410px;top:2620px;width:690px;font-size:16px;line-height:26px;color:var(--text)}
.quote-name{left:410px;top:2743px;font-size:14px;font-weight:600;color:var(--ink)}
.quote-role{left:410px;top:2767px;font-size:10px;color:var(--text)}
.stars{left:410px;top:2781px;font-size:12px;color:var(--orange-light);letter-spacing:1px}
.dots{left:574px;top:2864px;display:flex;gap:4px}
.dots span{width:15px;height:15px;border-radius:50%;background:var(--white)}
.dots span.on{background:var(--blue)}
.news-sub{left:0;top:3075px;width:1200px;text-align:center;font-size:21px;color:var(--ink)}
.news-input{left:251px;top:3147px;width:432px;height:68px;background:var(--blue);color:var(--white);font-size:16px;padding-left:15px;display:flex;align-items:center}
.news-btn{left:683px;top:3147px;width:266px;height:68px;background:var(--orange);color:var(--white);font-size:15px;font-weight:500;display:flex;align-items:center;justify-content:center}
.footer-bg{left:0;top:3200px}
.foot-brand{left:220px;top:3468px;text-align:center;color:var(--white);line-height:1}
.foot-brand b{font-size:62px;font-weight:700;letter-spacing:2px;display:block}
.foot-brand span{font-size:15px;font-weight:600;letter-spacing:1px}
.divider{top:3451px;width:1px;height:177px;background:#5b5f6a}
.foot-head{font-size:13px;font-weight:600;color:var(--white)}
.foot-text{font-size:12px;line-height:21px;color:var(--white)}
.foot-rule{left:85px;top:3628px;width:1030px;height:1px;background:#5b5f6a}
.copy{left:86px;top:3657px;font-size:12px;color:var(--white)}
.social.foot{left:972px;top:3647px}
.social.foot span{width:32px;height:32px;background:var(--orange)}
</style>
</head>
<body>
<div class="abs top-bar"></div>
<div class="abs brand"><span class="brand-name">KLV</span><span class="brand-sub">MESSAGING</span></div>
<nav class="abs main-nav"><span>About</span><span>Services</span><span>Industries</span><span>Portfolio</span><span>Clients</span><span>Contact</span></nav>
<div class="abs social head"><span></span><span></span><span></span><span></span></div>

<svg class="abs hero-bg" width="1200" height="510" viewBox="0 89 1200 510">
  <path d="M0 89 H1200 V488 Q600 660 0 488 Z" fill="var(--navy)"/>
  <path d="M0 488 Q600 660 1200 488" fill="none" stroke="var(--orange)" stroke-width="9"/>
</svg>
<div class="abs hero-photo" role="img" aria-label="Portrait of Marcus Holloway in a light blue shirt"></div>
<h1 class="abs hero-title">YOUR VOICE, <em>MY WORDS.</em></h1>
<p class="abs hero-sub">Copywriting and executive ghostwriting that speaks for<br>your vision and your technology.</p>
<div class="abs btn hero-btn">Read More</div>

<h2 class="abs section-title" style="top:664px">OUR <em>CLIENTS</em></h2>
<svg class="abs arrow" style="left:88px;top:802px" viewBox="0 0 30 40"><path d="M22 6 L9 20 L22 34" fill="none" stroke="var(--blue)" stroke-width="6"/></svg>
<svg class="abs arrow" style="left:1090px;top:802px" viewBox="0 0 30 40"><path d="M8 6 L21 20 L8 34" fill="none" stroke="var(--blue)" stroke-width="6"/></svg>
<div class="abs client" style="left:229px;top:766px"><i></i>Hivemark</div>
<div class="abs client" style="left:414px;top:766px">Corvane</div>
<div class="abs client" style="left:607px;top:766px">Paylume</div>
<div class="abs client" style="left:809px;top:766px">Nexora</div>
<div class="abs client" style="left:229px;top:851px;font-size:22px">Veridian Nets</div>
<div class="abs client" style="left:414px;top:851px">Taxlyne</div>
<div class="abs client" style="left:607px;top:851px">Querra</div>
<div class="abs client" style="left:809px;top:851px">Delphin AI</div>

<div class="abs grey-band" style="top:964px;height:765px"></div>
<h2 class="abs section-title" style="top:1038px">WHAT <em>I DO</em></h2>

<div class="abs card" style="left:85px"></div>
<div class="abs card" style="left:436px"></div>
<div class="abs card" style="left:789px"></div>
<div class="abs card-photo" style="left:133px;top:1148px" role="img" aria-label="Child looking through a spyglass"></div>
<div class="abs card-photo" style="left:484px;top:1148px" role="img" aria-label="Child writing on a chalkboard"></div>
<div class="abs card-photo" style="left:837px;top:1148px" role="img" aria-label="Child fishing by the water"></div>
<div class="abs card-icon" style="left:209px;top:1333px"><svg width="40" height="30" viewBox="0 0 40 30"><rect x="2" y="2" width="36" height="26" rx="3" fill="#fff"/><path d="M2 5 L20 17 L38 5" fill="none" stroke="var(--orange)" stroke-width="3"/></svg></div>
<div class="abs card-icon" style="left:560px;top:1333px"><svg width="30" height="38" viewBox="0 0 30 38"><rect x="2" y="2" width="26" height="34" rx="3" fill="none" stroke="#fff" stroke-width="3"/><path d="M8 12H22M8 19H22M8 26H22" stroke="#fff" stroke-width="3"/></svg></div>
<div class="abs card-icon" style="left:913px;top:1333px"><svg width="34" height="34" viewBox="0 0 34 34"><rect x="1" y="1" width="32" height="32" rx="9" fill="#fff"/><path d="M10 12H18M10 22H24" stroke="var(--orange)" stroke-width="4" stroke-linecap="round"/></svg></div>

<div class="abs card-title" style="left:85px;top:1437px">MESSAGING</div>
<div class="abs card-title" style="left:436px;top:1437px">COLLATERAL</div>
<div class="abs card-title" style="left:789px;top:1437px">CONTENT MARKETING</div>
<p class="abs card-text" style="left:85px;top:1471px">Lorem ipsum dolor sit amet, consectetur<br>adipiscing elit, sed do eiusmod tempor<br>incididunt ut labore et dolore magna</p>
<p class="abs card-text" style="left:436px;top:1471px">Lorem ipsum dolor sit amet, consectetur<br>adipiscing elit, sed do eiusmod tempor<br>incididunt ut labore et dolore magna</p>
<p class="abs card-text" style="left:789px;top:1471px">Lorem ipsum dolor sit amet, consectetur<br>adipiscing elit, sed do eiusmod tempor<br>incididunt ut labore et dolore magna</p>
<div class="abs btn card-btn" style="left:186px;top:1555px">Read More</div>
<div class="abs btn card-btn" style="left:537px;top:1555px">Read More</div>
<div class="abs btn card-btn" style="left:890px;top:1555px">Read More</div>

<div class="abs why-bg" role="img" aria-label="Blue-tinted desk with keyboard and notebook"></div>
<h2 class="abs why-title">WHY CHOOSE ME</h2>
<p class="abs why-text">Since 2001, KLV Messaging has had the opportunity to create collateral and content for tens of companies across a wide range of industries. Following is a small selection of recent projects:</p>
<ul class="abs why-list">
  <li>Contributed Content</li><li>Blog Content</li><li>White Papers &amp; E-Books</li><li>Case Studies</li><li>Web Site Content</li><li>Video - Concept and Script</li><li>Press Releases</li><li>Collateral (brochures, datasheets and more)</li>
</ul>
<div class="abs why-photo" role="img" aria-label="Portrait of Marcus Holloway standing"></div>

<div class="abs grey-band" style="top:2414px;height:545px"></div>
<h2 class="abs section-title" style="top:2490px">WHAT THEY’RE <em>SAYING</em></h2>
<div class="abs quote-circle"></div>
<div class="abs quote-mark">“</div>
<div class="abs client-photo" role="img" aria-label="Photo of client Dana Whitfield"></div>
<p class="abs quote-text">Marcus is more than an extraordinary copywriter; he is a unique marketing professional. Marcus has the rare talent of really listening to the customer; quickly (but deeply) understanding their industry and products, objectives and needs; and then quickly turning it all into clear and creative marketing messages and collateral.</p>
<div class="abs quote-name">Dana Whitfield</div>
<div class="abs quote-role">CMO, Corliss Media</div>
<div class="abs stars">★★★★★</div>
<div class="abs dots"><span class="on"></span><span></span><span></span></div>

<h2 class="abs section-title" style="top:3027px">SIGN UP FOR OUR <em>NEWSLETTER</em></h2>
<p class="abs news-sub">Submit your Email address to receive latest updates</p>
<div class="abs news-input">Enter Email Here</div>
<div class="abs news-btn">SIGNUP</div>

<svg class="abs footer-bg" width="1200" height="498" viewBox="0 3200 1200 498">
  <path d="M0 3401 Q600 3223 1200 3401 V3698 H0 Z" fill="var(--navy)"/>
  <path d="M0 3401 Q600 3223 1200 3401" fill="none" stroke="var(--orange)" stroke-width="9"/>
</svg>
<div class="abs foot-brand"><b>KLV</b><span>MESSAGING</span></div>
<div class="abs divider" style="left:452px"></div>
<div class="abs divider" style="left:729px"></div>
<svg class="abs" style="left:495px;top:3470px" width="22" height="30" viewBox="0 0 22 30"><path d="M11 1C5 1 1 5.5 1 11c0 7 10 18 10 18s10-11 10-18C21 5.5 17 1 11 1z" fill="var(--orange)"/><circle cx="11" cy="11" r="4" fill="var(--navy)"/></svg>
<div class="abs foot-head" style="left:534px;top:3476px">VISIT US AT</div>
<p class="abs foot-text" style="left:534px;top:3505px">KLV Messaging,<br>P.O. Box 1250<br>Lavon, Israel 40100</p>
<svg class="abs" style="left:771px;top:3468px" width="28" height="28" viewBox="0 0 28 28"><path d="M6 3l5 5-3 3c2 4 5 7 9 9l3-3 5 5-4 4C12 25 3 16 2 7z" fill="var(--orange)"/></svg>
<div class="abs foot-head" style="left:812px;top:3474px">CONTACT US</div>
<p class="abs foot-text" style="left:812px;top:3505px">Phone: +972-54-000-1122<br>Email: hello@klvmsg.co.il</p>
<div class="abs foot-rule"></div>
<div class="abs copy">Copyright © 2022 KLV Messaging</div>
<div class="abs social foot"><span></span><span></span><span></span><span></span></div>
</body>
</html>
```